20 years in Business Magazine Ad

We need a half page advertisement, celebrating 20 years in business in 2016. We are a globalized Flavor and Fragrance Ingredient company called Durvanox Corp. I've attached a file of our current logos. I like the idea of the Globe with pearls- but we definitely need an updated version of it. Plus room for the website address, phone number and email address.

Industry/Entity Type

Business

Requirements
Must have
• Wording saying that we are celebrating 20 years in business
Nice to have
• Something that says to the reader that we are a global company

```html
<!DOCTYPE html>
<html lang="en">
<head>
<meta charset="utf-8">
<title>Durvanox Corp – 20 Years In Business</title>
<link rel="stylesheet" href="https://fonts.googleapis.com/css2?family=Great+Vibes&family=Jost:wght@400&display=swap">
<style>
  :root {
    --page-bg: #e9e9ec;
    --ad-white: #ffffff;
    --pearl-light: #f7f7f8;
    --pearl-mid: #e4e4e7;
    --pearl-shadow: #cfcfd4;
    --ink-navy: #2a2d8c;
    --ink-dark: #2b2b33;
    --accent-peach: #f2c9b8;
  }
  * { margin: 0; padding: 0; box-sizing: border-box; }
  html, body {
    width: 1200px;
    height: 960px;
    overflow: hidden;
    background: var(--page-bg);
  }
  .ad {
    position: absolute;
    left: 0;
    top: 92px;
    width: 1200px;
    height: 776px;
    background: var(--ad-white);
    overflow: hidden;
  }
  .ad__backdrop {
    position: absolute;
    inset: 0;
    background:
      radial-gradient(ellipse 90% 55% at 50% 100%, var(--pearl-shadow) 0%, var(--pearl-mid) 45%, transparent 80%),
      linear-gradient(180deg, var(--ad-white) 0%, var(--pearl-light) 45%, var(--pearl-mid) 100%);
  }
  .brand {
    position: absolute;
    top: 132px;
    left: 0;
    width: 100%;
    display: flex;
    justify-content: center;
    align-items: center;
    gap: 14px;
  }
  .brand__dot {
    width: 30px;
    height: 30px;
    border-radius: 50%;
    background: var(--accent-peach);
  }
  .brand__name {
    font-family: "Jost", sans-serif;
    font-weight: 400;
    font-size: 58px;
    line-height: 1;
    color: var(--ink-navy);
    letter-spacing: 1px;
  }
  .headline {
    position: absolute;
    left: 0;
    width: 100%;
    text-align: center;
    font-family: "Great Vibes", cursive;
    font-weight: 400;
    color: var(--ink-navy);
    line-height: 1;
  }
  .headline--first { top: 300px; font-size: 92px; }
  .headline--second { top: 410px; font-size: 118px; }
  .contact {
    position: absolute;
    font-family: "Jost", sans-serif;
    font-size: 24px;
    color: var(--ink-dark);
    line-height: 1;
  }
  .contact__label { color: var(--ink-navy); }
  .contact--web { left: 114px; top: 712px; color: var(--ink-navy); }
  .contact--phone { right: 68px; top: 668px; }
  .contact--email { right: 68px; top: 712px; }
</style>
</head>
<body>
  <main class="ad">
    <div class="ad__backdrop" role="img" aria-label="Soft-focus photograph of white pearls with strands of small pearls curving across the lower left"></div>

    <div class="brand">
      <span class="brand__dot"></span>
      <span class="brand__name">Durvanox</span>
    </div>

    <h1 class="headline headline--first">We Are Celebrating</h1>
    <p class="headline headline--second">20 Years In Business</p>

    <p class="contact contact--web">www.durvanoxcorp.com</p>
    <p class="contact contact--phone"><span class="contact__label">CALL US -</span> 1234 5678 90</p>
    <p class="contact contact--email"><span class="contact__label">Email -</span> order@durvanoxcorp.com</p>
  </main>
</body>
</html>
```